Small Business Consulting Firm Needs Business Card Design

Need a sleek modern business card with 2 sides matching the colors of our logo. We will be placing these with a mailer we are sending out. These business cards will only ever be given to business owners. We operate helping businesses who are struggling with cash flow or finances. If the green and blue design needs to be moved to the right of "Harborline Crest Consulting" for aesthetic purposes that is ok. We will need an editable file if possible. We would like to include the reps name, email, website, and phone number. For now just use Peter Vance, pvance@harborlinecrest.com, www.harborlinecrest.com, and 833-555-0172.

```html
<!DOCTYPE html>
<html lang="en">
<head>
<meta charset="utf-8">
<title>Harborline Crest Consulting – Business Card</title>
<link rel="stylesheet" href="https://fonts.googleapis.com/css2?family=Lato:wght@400;700&display=swap">
<style>
  :root {
    --backdrop: #666a6d;
    --card: #ffffff;
    --blue: #1479c4;
    --blue-deep: #0d5c99;
    --green: #6cb33f;
    --green-deep: #4f8f2a;
    --ink: #3d3d3d;
    --ink-soft: #6d6d6d;
  }
  * { margin: 0; padding: 0; box-sizing: border-box; }
  html, body {
    width: 1200px; height: 1056px; overflow: hidden;
    background: var(--backdrop);
    font-family: "Lato", sans-serif;
  }
  .card {
    position: absolute; left: 220px;
    width: 760px; height: 434px;
    background: var(--card);
    overflow: hidden;
    box-shadow: 0 6px 18px rgba(0,0,0,.35);
  }
  .card--contact { top: 70px; }
  .card--brand { top: 552px; }
  .card__art { position: absolute; inset: 0; width: 100%; height: 100%; }

  .contact { position: absolute; left: 170px; top: 178px; width: 300px; }
  .contact__name {
    font-size: 30px; font-weight: 700; color: var(--blue);
    padding-bottom: 4px; border-bottom: 2px solid var(--green);
  }
  .contact__list { list-style: none; margin-top: 10px; }
  .contact__item {
    display: flex; align-items: center; gap: 12px;
    font-size: 17px; color: var(--ink-soft); line-height: 28px;
  }
  .contact__icon { width: 14px; height: 14px; fill: var(--green); flex: none; }

  .brand {
    position: absolute; left: 0; right: 0; top: 120px;
    display: flex; flex-direction: column; align-items: center;
    color: var(--ink); font-weight: 400;
  }
  .brand__square { width: 64px; height: 64px; background: var(--green); margin-bottom: 34px; }
  .brand__name { font-size: 34px; letter-spacing: 3px; }
  .brand__tag { font-size: 16px; letter-spacing: 9px; margin-top: 6px; }
</style>
</head>
<body>

<section class="card card--contact">
  <svg class="card__art" viewBox="0 0 760 434" aria-hidden="true">
    <polygon points="0,150 110,230 0,300" fill="var(--blue)"/>
    <polygon points="0,230 110,230 0,300" fill="var(--blue-deep)"/>
    <polygon points="760,20 600,210 760,340" fill="var(--green)"/>
    <polygon points="760,210 600,210 760,340" fill="var(--green-deep)"/>
  </svg>
  <div class="contact">
    <h1 class="contact__name">Peter Vance</h1>
    <ul class="contact__list">
      <li class="contact__item">
        <svg class="contact__icon" viewBox="0 0 16 16"><path d="M3 1l3 3-2 2c1 2 3 4 5 5l2-2 3 3-2 3C6 15 1 10 1 3z"/></svg>
        833-555-0172
      </li>
      <li class="contact__item">
        <svg class="contact__icon" viewBox="0 0 16 16"><path d="M1 3h14v10H1z M1 3l7 6 7-6" stroke="#fff" stroke-width="1.2"/></svg>
        pvance@harborlinecrest.com
      </li>
      <li class="contact__item">
        <svg class="contact__icon" viewBox="0 0 16 16"><circle cx="8" cy="8" r="7"/><path d="M1 8h14M8 1c-3 4-3 10 0 14M8 1c3 4 3 10 0 14" stroke="#fff" stroke-width="1" fill="none"/></svg>
        www.harborlinecrest.com
      </li>
    </ul>
  </div>
</section>

<section class="card card--brand">
  <svg class="card__art" viewBox="0 0 760 434" aria-hidden="true">
    <polygon points="640,0 760,0 760,90" fill="var(--blue)"/>
    <polygon points="700,0 760,0 760,90" fill="var(--blue-deep)"/>
    <polygon points="0,300 0,434 230,434" fill="var(--green)"/>
    <polygon points="0,380 0,434 230,434" fill="var(--green-deep)"/>
  </svg>
  <div class="brand">
    <div class="brand__square"></div>
    <div class="brand__name">HARBORLINE CREST</div>
    <div class="brand__tag">CONSULTING</div>
  </div>
</section>

</body>
</html>
```